Premium Personal Brand — Facebook Banner (Used Across All Platforms)

Update — Additional Color Direction
In addition to the dark charcoal/slate direction already described, I'm also interested in seeing variants with:
Dark navy blue — Deep, authoritative, intelligence-community feel. Same textured/matte treatment, not flat or bright.
Warm charcoal with steel blue accent — Keep the dark base but introduce a subtle steel blue gradient, accent line, or tonal shift. Sophisticated, modern, adds dimension without adding color noise.
Both should maintain the same premium, restrained, architectural feel described in the original brief. No bright blues, no corporate PowerPoint energy — think midnight, think depth, think weight.
Everything else in the brief remains the same.
I am building a premium personal brand as an executive advisor to founders ($5M+ revenue).
This contest is Facebook-banner–focused, but the design must represent a visual system that will be reused across:
- LinkedIn
- YouTube
I- nstagram
- X (Twitter)
- Website hero sections and other brand touchpoints
Think of the Facebook banner as the primary expression of the brand — not a one-off graphic.
This project is about discovering a high-end visual style and brand feel, not decoration.
What to design
Please submit one cohesive visual system, shown primarily as:
- Facebook banner (primary focus)
The same design language should clearly translate to all platforms listed above.
Designers are responsible for using the current recommended dimensions for each platform.
Quick clarification on background direction:
Backgrounds should have depth and texture, not flat color fields. Avoid pure white, light grey, or solid black backgrounds. Think matte, architectural materials — stone, graphite, concrete, steel — not blank canvases. Subtle tonal variation is encouraged. Obvious gradients or decorative patterns are not.
Text to use
Primary Headline:
- Your Business Is Too Valuable To Be Run On Hope.
Subheadline:
- You didn’t build a business to become its prisoner.
Name:
Paul Whitaker
The headline should be the dominant visual element.
Logo note (important)
My personal logo is currently being finalized.
For this contest:
- Use a simple “PW” monogram placeholder
- Clean, bold, geometric sans-serif
- Do not design a logo
- The winning design must allow an easy logo swap later.
Headshot note (important)
- Please do not include a headshot in the banner design.
- Most platforms display a circular profile image separately.
- The banner should stand on its own using typography, layout, and tone only.
- Design the banner assuming the profile photo will sit nearby, not inside the banner.
Style direction
The design should feel:
- Premium
- Calm
- Confident
- Restrained
- High-trust
- Dark, neutral backgrounds are preferred.
- Fewer elements are better than more.
Think:
- Owner-level advisor
- Private equity / boardroom tone
- Industrial, Modern, Minimalist, Elite, Architectural, not decorative
What to avoid
Please do not submit designs that feel:
- Promotional, hype-driven, or salesy
- Like a coach, guru, or agency
- Bright, colorful, or gradient-heavy
- Busy or over-designed
- Based on stock photos
- No motivational speaker energy.
Reaction test
- If someone sees this banner on Facebook (or later on LinkedIn, YouTube, etc.), the reaction should be:
“That person is serious. I’d trust them with important decisions.”
Final note
- I am not looking for many variations.
- I am looking for one strong visual direction you believe in.
Simple beats clever.
- Restraint beats decoration.

```html
<!DOCTYPE html>
<html lang="en">
<head>
<meta charset="utf-8">
<title>Paul Whitaker — Banner</title>
<link href="https://fonts.googleapis.com/css2?family=Inter:ital,wght@0,400;0,700;0,800;1,400;1,700&display=swap" rel="stylesheet">
<style>
  :root {
    --page-bg: #e2e4d8;
    --banner-bg: #13171a;
    --headline: #e2e2e2;
    --white: #ffffff;
    --accent: #00e1f2;
  }
  html, body {
    margin: 0;
    padding: 0;
    width: 1200px;
    height: 725px;
    overflow: hidden;
    background: var(--page-bg);
    font-family: "Inter", Arial, sans-serif;
  }
  .banner {
    position: absolute;
    left: 30px;
    top: 222px;
    width: 1140px;
    height: 281px;
    background: var(--banner-bg);
    border-radius: 3px 3px 0 0;
    overflow: hidden;
  }
  .monogram {
    position: absolute;
    left: 35px;
    top: 15px;
    margin: 0;
    font-size: 35px;
    line-height: 40px;
    font-weight: 700;
    letter-spacing: 0.5px;
    color: var(--white);
  }
  .headline {
    position: absolute;
    left: 340px;
    top: 77px;
    margin: 0;
    font-size: 47px;
    line-height: 41px;
    font-weight: 400;
    letter-spacing: 2px;
    color: var(--headline);
  }
  .headline em {
    font-style: italic;
    font-weight: 700;
    letter-spacing: 1.5px;
  }
  .headline .stop {
    color: var(--accent);
  }
  .subline {
    position: absolute;
    left: 345px;
    top: 215px;
    margin: 0;
    font-size: 19px;
    line-height: 24px;
    font-style: italic;
    font-weight: 400;
    letter-spacing: 0.6px;
    color: var(--accent);
  }
  .name {
    position: absolute;
    right: 42px;
    top: 222px;
    margin: 0;
    font-size: 27px;
    line-height: 34px;
    font-weight: 800;
    letter-spacing: -1px;
    color: var(--white);
    white-space: nowrap;
  }
</style>
</head>
<body>
  <section class="banner">
    <p class="monogram">PW</p>
    <h1 class="headline">Your <em>Business</em> Is Too<br><em>Valuable</em> To Be Run<br>On Hope<span class="stop">.</span></h1>
    <p class="subline">You didn’t build a business to become it’s prisoner.</p>
    <p class="name">Paul Whitaker</p>
  </section>
</body>
</html>
```